QLindex warden tap - styling

We have a prototyped single page application. The content is in place what we need is restyling to

- make it more user friendly
- modern look and feel
- improve accessibility features
- use our brand guidelines (screen shots attached of the full website)

Prototype is available at http://boardviewapp.examplehost.net/

Target form factor:
Primary - tablet
Secondary - desktop

Target Market(s)

Business users - not financial professionals but people working for big companies who have some limited training in the concepts

Number of Pages Required

1 page

Requirements
Must have
• Touch user interface

```html
<!DOCTYPE html>
<html lang="en">
<head>
<meta charset="utf-8">
<title>QLindex warden tap – Flight Plan</title>
<link rel="stylesheet" href="https://fonts.googleapis.com/css2?family=Titillium+Web:wght@400;600;700&display=swap">
<style>
  :root {
    --brand-blue: #0f5fb5;
    --brand-blue-dark: #0b4f98;
    --menu-blue: #4aa8e6;
    --page-bg: #e8edf1;
    --canvas-bg: #f4f6f8;
    --card: #ffffff;
    --rule: #e3e8ec;
    --text: #5b6670;
    --text-muted: #8c959c;
    --icon: #d9dde0;
    --magenta: #b0327f;
    --plan-line: #9c0f5f;
    --actual-line: #3ea2e4;
    --fan-outer: #edf4f8;
    --fan-inner: #dfeaf2;
    --up: #3cbf6c;
    --down: #e06060;
    --tip-bg: #3b3b3b;
    --tip-accent: #ff8f8f;
    --track: #0a4788;
    --track-fill: #4aa8e6;
  }
  * { box-sizing: border-box; margin: 0; padding: 0; }
  html, body { width: 1200px; height: 998px; overflow: hidden; }
  body {
    background: var(--canvas-bg);
    font-family: "Titillium Web", Arial, sans-serif;
    color: var(--text);
  }
  .app {
    position: absolute; left: 0; top: 60px;
    width: 1200px; height: 878px;
    background: var(--page-bg);
    overflow: hidden;
  }
  /* header */
  .topbar {
    position: absolute; left: 0; top: 0; width: 1200px; height: 57px;
    background: var(--brand-blue); color: #fff;
  }
  .brand {
    position: absolute; left: 19px; top: 0; width: 98px; height: 57px;
    display: flex; align-items: center;
    font-size: 22px; font-weight: 700; letter-spacing: -0.5px;
    border-right: 1px solid rgba(255,255,255,0.15);
  }
  .brand { left: 0; padding-left: 19px; width: 117px; }
  .menu { position: absolute; top: 0; height: 57px; display: flex; align-items: center;
    justify-content: center; gap: 14px; font-size: 13.5px; font-weight: 600;
    border-left: 1px solid rgba(255,255,255,0.15); }
  .menu::after { content: ""; border: 4px solid transparent; border-top: 5px solid #fff; margin-top: 5px; }
  .menu.no-caret::after { display: none; }
  .menu--company { left: 530px; width: 144px; background: var(--brand-blue-dark); }
  .menu--scheme { left: 674px; width: 199px; }
  .menu--basis { left: 873px; width: 186px; }
  .menu--date { left: 1059px; width: 141px; }
  .dropdown {
    position: absolute; left: 530px; top: 57px; width: 144px;
    background: var(--menu-blue); color: #fff; font-size: 13.5px; z-index: 5;
  }
  .dropdown li { list-style: none; height: 37px; line-height: 37px; padding-left: 25px; }
  .dropdown li + li { border-top: 1px solid rgba(255,255,255,0.25); }

  /* main card */
  .card { position: absolute; left: 23px; top: 81px; width: 1152px; height: 637px; background: var(--card); }
  .kpis { position: absolute; left: 0; top: 0; width: 1152px; height: 107px; display: flex;
    border-bottom: 1px solid var(--rule); }
  .kpi { position: relative; height: 107px; border-right: 1px solid var(--rule); }
  .kpi:last-child { border-right: none; }
  .kpi svg { position: absolute; left: 28px; top: 24px; }
  .kpi-value { position: absolute; right: 24px; top: 22px; font-size: 34px; font-weight: 600; color: #666f77; line-height: 1; }
  .kpi-value.up { color: var(--up); }
  .kpi-value.down { color: var(--down); }
  .kpi-value .arrow { font-size: 18px; vertical-align: top; margin-right: 3px; }
  .kpi-label { position: absolute; right: 22px; top: 72px; font-size: 10.5px; font-weight: 600; color: var(--text-muted);
    display: flex; align-items: center; gap: 7px; }
  .kpi-label::after { content: ""; border: 5px solid transparent; border-top: 6px solid #7b848b; margin-top: 5px; }

  .chart-title { position: absolute; left: 43px; top: 144px; font-size: 35px; font-weight: 400; color: var(--magenta); }
  .chart { position: absolute; left: -23px; top: 209px; }
  .axis-label { font-family: "Titillium Web", Arial, sans-serif; font-size: 12.5px; fill: var(--text-muted); }

  .tooltip {
    position: absolute; left: 504px; top: 225px; width: 195px; height: 145px;
    background: var(--tip-bg); color: #fff; border-radius: 2px; font-size: 12.5px; z-index: 3;
  }
  .tooltip::after { content: ""; position: absolute; left: 90px; bottom: -10px;
    border: 8px solid transparent; border-top: 10px solid var(--tip-bg); border-bottom: 0; }
  .tooltip dl { position: absolute; left: 17px; top: 20px; display: grid;
    grid-template-columns: 94px 90px; row-gap: 2px; }
  .tooltip dd { display: inline; color: var(--tip-accent); font-weight: 600; }
  .tooltip dt { display: inline; }
  .tooltip .stat { line-height: 18px; }
  .tooltip-date { position: absolute; left: 0; width: 100%; top: 104px; text-align: center; font-size: 17px; }

  /* controls */
  .controls { position: absolute; left: 0; top: 637px; width: 1152px; height: 135px;
    background: var(--brand-blue); color: #fff; }
  .controls-lock { position: absolute; left: 0; top: 0; width: 94px; height: 135px;
    border-right: 1px solid rgba(255,255,255,0.15); display: flex; align-items: center; justify-content: center; }
  .control { position: absolute; top: 0; height: 135px; }
  .control--strategy { left: 94px; width: 540px; border-right: 1px solid rgba(255,255,255,0.15); }
  .control--contrib { left: 634px; width: 518px; }
  .control h2 { position: absolute; left: 74px; top: 31px; font-size: 13.5px; font-weight: 700; letter-spacing: 0.3px; }
  .control--contrib h2 { left: 47px; }
  .slider { position: absolute; left: 74px; top: 69px; width: 413px; height: 6px; border-radius: 3px; background: var(--track); }
  .control--contrib .slider { left: 47px; }
  .slider-fill { position: absolute; left: 0; top: 0; height: 6px; border-radius: 3px; background: var(--track-fill); }
  .slider-knob { position: absolute; top: -8px; width: 22px; height: 22px; border-radius: 50%; background: #fff; margin-left: -11px; }
  .slider-labels { position: absolute; left: 74px; top: 84px; width: 413px; font-size: 14px; display: flex; justify-content: space-between; }
  .control--contrib .slider-labels { left: 47px; }
  .slider-value { position: absolute; top: 84px; font-size: 17px; font-weight: 700; transform: translateX(-50%); }
</style>
</head>
<body>
<div class="app">
  <header class="topbar">
    <div class="brand">QLindex</div>
    <div class="menu menu--company">XYZ Limited</div>
    <div class="menu menu--scheme">XYZ Pension Scheme</div>
    <div class="menu menu--basis">Technical Provisions</div>
    <div class="menu menu--date">October 2014</div>
  </header>
  <ul class="dropdown">
    <li>XYZ Limited</li>
    <li>PQR Corporation</li>
  </ul>

  <main class="card">
    <section class="kpis">
      <div class="kpi" style="width:292px">
        <svg width="75" height="60" viewBox="0 0 75 60" fill="none" stroke="var(--icon)" stroke-width="2.5" aria-hidden="true">
          <ellipse cx="17" cy="8" rx="14" ry="5"/><path d="M3 8v44c0 3 6 5 14 5s14-2 14-5V8M3 19c0 3 6 5 14 5s14-2 14-5M3 30c0 3 6 5 14 5s14-2 14-5M3 41c0 3 6 5 14 5s14-2 14-5"/>
          <ellipse cx="54" cy="33" rx="14" ry="5"/><path d="M40 33v19c0 3 6 5 14 5s14-2 14-5V33M40 43c0 3 6 5 14 5s14-2 14-5"/>
        </svg>
        <div class="kpi-value">91%</div>
        <div class="kpi-label">Funding Level</div>
      </div>
      <div class="kpi" style="width:286px">
        <svg width="65" height="62" viewBox="0 0 65 62" fill="none" stroke="var(--icon)" stroke-width="3" aria-hidden="true">
          <circle cx="14" cy="14" r="11"/><circle cx="48" cy="48" r="11"/><path d="M50 3 12 59"/>
        </svg>
        <div class="kpi-value up"><span class="arrow">↑</span>2.5%</div>
        <div class="kpi-label">Funding Level Change</div>
      </div>
      <div class="kpi" style="width:288px">
        <svg width="75" height="58" viewBox="0 0 75 58" fill="none" stroke="var(--icon)" stroke-width="2.5" aria-hidden="true">
          <path d="M3 2v52h60M57 48l6 6-6 6"/><path d="M8 44 30 24l16 8 22-24"/><circle cx="30" cy="24" r="3"/><circle cx="46" cy="32" r="3"/>
        </svg>
        <div class="kpi-value down"><span class="arrow">↓</span>3%</div>
        <div class="kpi-label">Progress Against Flight Plan</div>
      </div>
      <div class="kpi" style="width:286px">
        <svg width="72" height="62" viewBox="0 0 72 62" fill="none" stroke="var(--icon)" stroke-width="2.5" aria-hidden="true">
          <path d="M2 60h68M8 60V36h10v24M28 60V4h10v56M48 60V20h10v40"/>
        </svg>
        <div class="kpi-value">67%</div>
        <div class="kpi-label">10-yr Projected Funding Level</div>
      </div>
    </section>

    <h1 class="chart-title">Flight Plan</h1>

    <svg class="chart" width="1200" height="400" viewBox="0 0 1200 400" role="img" aria-label="Flight plan chart: projected funding level range with actual and target lines">
      <g stroke="var(--rule)" stroke-width="1">
        <line x1="117" y1="15" x2="1146" y2="15"/>
        <line x1="117" y1="77.4" x2="1146" y2="77.4"/>
        <line x1="117" y1="139.8" x2="1146" y2="139.8"/>
        <line x1="117" y1="202.2" x2="1146" y2="202.2"/>
        <line x1="117" y1="264.6" x2="1146" y2="264.6"/>
        <line x1="117" y1="327" x2="1146" y2="327"/>
      </g>
      <g class="axis-label" text-anchor="end">
        <text x="102" y="19">160%</text><text x="102" y="81">140%</text><text x="102" y="144">120%</text>
        <text x="102" y="206">100%</text><text x="102" y="269">80%</text><text x="102" y="331">60%</text>
      </g>
      <polygon points="331,187 690,84 1146,106 1146,248 705,292" fill="var(--fan-outer)"/>
      <polygon points="331,187 690,94 1146,122 1146,234 705,278" fill="var(--fan-inner)"/>
      <polyline points="120,234 378,194 614,212 886,170 1037,178 1146,151" fill="none" stroke="var(--actual-line)" stroke-width="3" stroke-linejoin="round"/>
      <line x1="331" y1="212" x2="1146" y2="112" stroke="var(--plan-line)" stroke-width="3"/>
      <g class="axis-label" text-anchor="middle">
        <text x="150" y="376">30-Nov-13</text><text x="320" y="376">31-Jan-13</text><text x="486" y="376">31-Mar-13</text>
        <text x="659" y="376">31-May-13</text><text x="811" y="376">2014</text><text x="895" y="376">2015</text>
        <text x="980" y="376">2016</text><text x="1063" y="376">2017</text>
      </g>
      <path d="M1133 364l8 6-8 6z" fill="var(--brand-blue)"/>
    </svg>

    <div class="tooltip" role="tooltip">
      <dl>
        <div class="stat"><dt>05th: </dt><dd>90%</dd></div>
        <div class="stat"><dt>75th: </dt><dd>451%</dd></div>
        <div class="stat"><dt>25th: </dt><dd>121%</dd></div>
        <div class="stat"><dt>95th: </dt><dd>143%</dd></div>
        <div class="stat"><dt>50th: </dt><dd>324%</dd></div>
      </dl>
      <div class="tooltip-date">10/14/2014</div>
    </div>

    <section class="controls">
      <div class="controls-lock">
        <svg width="24" height="30" viewBox="0 0 24 30" aria-label="Unlocked" role="img">
          <path d="M6 13V8a6 6 0 0 1 12 0v1" fill="none" stroke="#fff" stroke-width="3"/>
          <rect x="1" y="13" width="22" height="16" rx="2" fill="#fff"/>
          <rect x="10" y="18" width="4" height="6" fill="var(--brand-blue)"/>
        </svg>
      </div>
      <div class="control control--strategy">
        <h2>INVESTMENT STRATEGY</h2>
        <div class="slider"><div class="slider-fill" style="width:151px"></div><div class="slider-knob" style="left:151px"></div></div>
        <div class="slider-labels"><span>Matching</span><span>Growth</span></div>
        <div class="slider-value" style="left:225px">54%/36</div>
      </div>
      <div class="control control--contrib">
        <h2>CONTRIBUTIONS</h2>
        <div class="slider"><div class="slider-fill" style="width:151px"></div><div class="slider-knob" style="left:151px"></div></div>
        <div class="slider-labels"><span>£0m</span><span>£30m</span></div>
        <div class="slider-value" style="left:198px">£15.0m</div>
      </div>
    </section>
  </main>
</div>
</body>
</html>
```